Veltarum

Standard Business Card design.
Sample two-sided design uploaded. White front, Black back.
Would like white shield to be on all black background side.
Willing to look at a couple creative designs, but nothing crazy.
Preference for a classic, confident, strong design.

```html
<!DOCTYPE html>
<html lang="en">
<head>
<meta charset="utf-8">
<title>Veltarum Business Card</title>
<link href="https://fonts.googleapis.com/css2?family=Montserrat:wght@400;500;700&display=swap" rel="stylesheet">
<style>
  :root {
    --stage: #1f1f21;
    --card-front: #ffffff;
    --card-back: #141414;
    --ink: #111111;
    --ink-soft: #3a3a3a;
    --rule: #1a1a1a;
    --back-text: #ffffff;
  }
  * { margin: 0; padding: 0; box-sizing: border-box; }
  html, body { width: 1200px; height: 800px; overflow: hidden; }
  body {
    background: var(--stage);
    font-family: "Montserrat", sans-serif;
    display: flex;
    align-items: center;
    justify-content: center;
    gap: 40px;
  }
  .card {
    width: 540px;
    height: 310px;
    border-radius: 22px;
    position: relative;
    overflow: hidden;
  }
  .card-front { background: var(--card-front); color: var(--ink); }
  .card-back {
    background: var(--card-back);
    display: flex;
    align-items: center;
    justify-content: center;
  }
  .brand {
    position: absolute;
    left: 38px;
    top: 40px;
    display: flex;
    align-items: center;
    gap: 12px;
  }
  .brand-mark {
    width: 18px; height: 18px;
    background: var(--ink);
  }
  .brand-name {
    font-weight: 700;
    font-size: 30px;
    letter-spacing: 3px;
    text-transform: uppercase;
  }
  .identity {
    position: absolute;
    right: 36px;
    top: 58px;
    text-align: right;
    width: 300px;
  }
  .person-name {
    font-weight: 700;
    font-size: 24px;
    letter-spacing: 0.5px;
    text-transform: uppercase;
  }
  .identity-rule {
    height: 1.5px;
    background: var(--rule);
    margin: 8px 0 6px;
  }
  .person-role {
    font-size: 12px;
    letter-spacing: 1.5px;
    text-transform: uppercase;
    color: var(--ink-soft);
  }
  .address {
    margin-top: 18px;
    font-size: 13.5px;
    line-height: 1.45;
    color: var(--ink-soft);
  }
  .contact {
    position: absolute;
    left: 38px;
    bottom: 30px;
    width: 230px;
  }
  .contact-rule { height: 1.5px; background: var(--rule); margin-bottom: 10px; }
  .contact-list { list-style: none; }
  .contact-item {
    display: flex;
    align-items: center;
    gap: 9px;
    font-size: 13.5px;
    line-height: 1.6;
  }
  .contact-icon { width: 12px; height: 12px; flex: none; }
  .back-name {
    color: var(--back-text);
    font-weight: 700;
    font-size: 40px;
    letter-spacing: 6px;
    text-transform: uppercase;
  }
</style>
</head>
<body>
  <section class="card card-front">
    <div class="brand">
      <span class="brand-mark"></span>
      <span class="brand-name">Veltarum</span>
    </div>
    <div class="identity">
      <h1 class="person-name">Marcus Hale</h1>
      <div class="identity-rule"></div>
      <p class="person-role">Managing Director</p>
      <p class="address">18, Harbour Row<br>Larkfield 20931,<br>Northland</p>
    </div>
    <div class="contact">
      <div class="contact-rule"></div>
      <ul class="contact-list">
        <li class="contact-item">
          <svg class="contact-icon" viewBox="0 0 24 24"><path fill="#111" d="M6.6 10.8a15.1 15.1 0 0 0 6.6 6.6l2.2-2.2c.3-.3.7-.4 1-.2 1.1.4 2.3.6 3.6.6.6 0 1 .4 1 1V20c0 .6-.4 1-1 1A17 17 0 0 1 3 4c0-.6.4-1 1-1h3.5c.6 0 1 .4 1 1 0 1.3.2 2.5.6 3.6.1.3 0 .7-.2 1z"/></svg>
          044-555 012 347
        </li>
        <li class="contact-item">
          <svg class="contact-icon" viewBox="0 0 24 24"><path fill="#111" d="M2 5h20v14H2z"/><path fill="none" stroke="#fff" stroke-width="1.6" d="M2.5 5.5 12 13l9.5-7.5"/></svg>
          info@veltarum.com
        </li>
        <li class="contact-item">
          <svg class="contact-icon" viewBox="0 0 24 24"><g fill="none" stroke="#111" stroke-width="2"><circle cx="12" cy="12" r="10"/><path d="M2 12h20M12 2c3 3 3 17 0 20M12 2c-3 3-3 17 0 20"/></g></svg>
          www.veltarum.com
        </li>
      </ul>
    </div>
  </section>
  <section class="card card-back">
    <span class="back-name">Veltarum</span>
  </section>
</body>
</html>
```